New Public Cloud Consulting Needs Powerpoint Template

Setting up a new consulting practice and need a powerpoint template and design that reflects our vision. We focus on KLV Public Cloud only. We want to emphasize innovation, cloud, speed. We are based in Asia, with headquarters in Singapore. We serve Asia and Europe customers. The attached file is the current template and logo that we use. However it is not dynamic enough. Blue is the color of our logo - but we must have other colors that complement the blue.

Target Market(s)

Innovation, cloud, advisory

Font styles to use
Other font styles liked:
• We want a different font that what is included in the file.

Requirements
Must have
• Logo which is included in the sample template and blue color - however we want other colors included. To date - most of the designs are completely blue - which we do not want. Additionally we need to create an image of innovation, future vision. Please do not include a picture of a cloud. That is not innovative.
Nice to have
• Would be nice to show people in some of the slides - professional etc. There is one slide in the attached presentation that gives you an idea of this concept. How else can we do this ?

```html
<!DOCTYPE html>
<html lang="en">
<head>
<meta charset="utf-8">
<title>VELA – Cloud Advisory Deck</title>
<link href="https://fonts.googleapis.com/css2?family=Barlow:ital,wght@0,400;0,500;0,600;1,500;1,700&family=Barlow+Condensed:wght@500;600;700&display=swap" rel="stylesheet">
<style>
:root{
  --blue:#2a5bd7;
  --blue-dark:#1e44a8;
  --navy:#1b2a5c;
  --cyan:#14c4ea;
  --green:#1fbf7f;
  --slate:#6b7a99;
  --grey:#8e97a8;
  --ink:#3b4150;
  --mute:#9aa2b1;
  --band:#eef0f4;
  --panel:#eef2f8;
  --red:#f2546a;
  --page:#ffffff;
}
*{margin:0;padding:0;box-sizing:border-box}
html,body{width:1200px;height:1003px;overflow:hidden;background:var(--page)}
.deck{position:relative;width:1200px;height:1003px}
.slide{position:absolute;width:400px;height:226px;overflow:hidden;background:#fff;box-shadow:0 0 0 .5px #eceef2}
.slide svg{display:block;width:400px;height:226px}
.h{font-family:"Barlow Condensed",sans-serif;font-weight:600;fill:var(--blue)}
.h2{font-family:"Barlow",sans-serif;font-weight:600;fill:var(--blue)}
.b{font-family:"Barlow",sans-serif;fill:var(--ink)}
.brand{font-family:"Barlow",sans-serif;font-weight:600;fill:var(--blue)}
.num{font-family:"Barlow",sans-serif;fill:var(--mute);font-size:3.5px}
.r1{top:23px}.r2{top:260px}.r3{top:498px}.r4{top:736px}
.c1{left:0}.c2{left:400px}.c3{left:800px}
</style>
</head>
<body>
<svg width="0" height="0" style="position:absolute">
  <defs>
    <symbol id="corner" viewBox="0 0 30 30">
      <polygon points="8,30 30,6 30,14 16,30" fill="#2a5bd7"/>
      <polygon points="18,30 30,17 30,30" fill="#7fa3ee"/>
      <polygon points="2,30 24,6 27,6 5,30" fill="#c7d5f5"/>
    </symbol>
    <symbol id="footer-brand" viewBox="0 0 40 10">
      <circle cx="3" cy="5" r="2.6" fill="#2a5bd7"/>
      <text x="7.5" y="8" class="brand" font-size="8">VELA</text>
    </symbol>
    <linearGradient id="photoTone" x1="0" y1="0" x2="1" y2="1">
      <stop offset="0" stop-color="#c9cfd8"/><stop offset=".55" stop-color="#8f8a84"/><stop offset="1" stop-color="#4d5566"/>
    </linearGradient>
    <linearGradient id="officeTone" x1="0" y1="0" x2="1" y2="0">
      <stop offset="0" stop-color="#5e5a52"/><stop offset=".5" stop-color="#a88f78"/><stop offset="1" stop-color="#3d3a36"/>
    </linearGradient>
    <linearGradient id="blueFade" x1="0" y1="0" x2="1" y2="1">
      <stop offset="0" stop-color="#2a5bd7"/><stop offset="1" stop-color="#1e44a8"/>
    </linearGradient>
    <linearGradient id="cyanFade" x1="0" y1="1" x2="1" y2="0">
      <stop offset="0" stop-color="#14c4ea" stop-opacity=".85"/><stop offset="1" stop-color="#2a5bd7" stop-opacity=".2"/>
    </linearGradient>
  </defs>
</svg>

<main class="deck">

<!-- Title -->
<section class="slide r1 c1">
<svg viewBox="0 0 400 226">
  <circle cx="24" cy="51" r="6" fill="var(--blue)"/>
  <text x="34" y="57" class="brand" font-size="17">VELA</text>
  <text class="h" font-size="21"><tspan x="20" y="95">Everyone Talks</tspan><tspan x="20" y="123">about Cloud &amp; Digital</tspan><tspan x="20" y="151">Transformation</tspan></text>
  <text x="20" y="170" font-family="Barlow,sans-serif" font-style="italic" font-weight="500" font-size="11" fill="var(--green)">We do it differently</text>
  <path d="M232 0 H400 V226 H172 L262 116 L206 82 Z" fill="url(#photoTone)" role="img" aria-label="Photo of a smiling team of young professionals talking together in a modern office"/>
  <polygon points="194,99 288,0 302,0 210,99" fill="var(--blue)"/>
  <polygon points="172,226 262,116 276,116 190,226" fill="var(--navy)"/>
  <polygon points="190,226 268,126 320,226" fill="url(#cyanFade)"/>
  <polygon points="262,116 305,60 340,113 300,170" fill="var(--cyan)" opacity=".35"/>
  <use href="#footer-brand" x="20" y="206" width="40" height="10"/>
</svg>
</section>

<!-- Discussion topics -->
<section class="slide r1 c2">
<svg viewBox="0 0 400 226">
  <path d="M0 0 H142 L202 113 L142 226 H0 Z" fill="url(#officeTone)" role="img" aria-label="Photo of colleagues gathered around a laptop in a bright office"/>
  <polygon points="110,0 138,0 223,113 195,113" fill="#c8cfdd"/>
  <polygon points="195,113 223,113 138,226 110,226" fill="#9fb0d6" opacity=".8"/>
  <polygon points="90,226 170,120 245,226" fill="var(--blue)" opacity=".9"/>
  <polygon points="0,226 60,150 110,226" fill="var(--cyan)" opacity=".55"/>
  <text x="233" y="56" class="h2" font-size="12.5">Discussion Topics</text>
  <g class="b" font-size="9.2">
    <text x="233" y="82"><tspan fill="var(--blue)">1.</tspan><tspan x="250">Branding</tspan></text>
    <text x="233" y="97"><tspan fill="var(--blue)">2.</tspan><tspan x="250">Offerings</tspan></text>
    <text x="233" y="113"><tspan fill="var(--blue)">3.</tspan><tspan x="250">Competitor Market</tspan></text>
    <text x="233" y="128"><tspan fill="var(--blue)">4.</tspan><tspan x="250">Organizational Structure</tspan></text>
    <text x="233" y="143"><tspan fill="var(--blue)">5.</tspan><tspan x="250">People Development</tspan></text>
    <text x="233" y="159"><tspan fill="var(--blue)">6.</tspan><tspan x="250">Timeline</tspan></text>
    <text x="233" y="174"><tspan fill="var(--blue)">7.</tspan><tspan x="250">Budget</tspan></text>
  </g>
  <text x="368" y="215" class="num">2</text>
  <use href="#corner" x="370" y="196" width="30" height="30"/>
</svg>
</section>

<!-- Focus -->
<section class="slide r1 c3">
<svg viewBox="0 0 400 226">
  <text x="20" y="23" class="h" font-size="18">Public Cloud is our Focus</text>
  <g class="b" font-size="10.6">
    <text x="20" y="53"><tspan fill="var(--blue)">•</tspan><tspan x="28">All Vela’s Services encompasses Public Cloud Core</tspan></text>
    <text x="20" y="74"><tspan fill="var(--blue)">•</tspan><tspan x="28">We focus on the journey to achieve digital transformation on the cloud</tspan></text>
    <text x="20" y="95"><tspan fill="var(--blue)">•</tspan><tspan x="28">Core Suite Public Cloud is the central backbone</tspan></text>
    <text x="20" y="116"><tspan fill="var(--blue)">•</tspan><tspan x="28">Our focus is on APAC and EMEA</tspan></text>
    <text x="20" y="137"><tspan fill="var(--blue)">•</tspan><tspan x="28">Our free assessments provide insights into your key challenges to</tspan></text>
    <text x="28" y="154">move to the cloud</text>
    <text x="20" y="175"><tspan fill="var(--blue)">•</tspan><tspan x="28">We transform your business processes to standardize on core Core</tspan></text>
  </g>
  <use href="#footer-brand" x="20" y="206" width="40" height="10"/>
  <text x="368" y="215" class="num">3</text>
  <use href="#corner" x="370" y="196" width="30" height="30"/>
</svg>
</section>

<!-- Pyramid -->
<section class="slide r2 c1">
<svg viewBox="0 0 400 226">
  <text x="20" y="22" class="h" font-size="18">Cloud Assessments &amp; Advisory Services</text>
  <g font-family="Barlow Condensed,sans-serif" font-weight="500" font-size="7.5" fill="var(--ink)">
    <rect x="131" y="50" width="136" height="13" rx="6.5" fill="#f4f5f8"/><text x="146" y="59">ROI Realization</text><circle cx="262" cy="56.5" r="7" fill="var(--blue)"/>
    <rect x="141" y="70" width="140" height="13" rx="6.5" fill="#f4f5f8"/><text x="157" y="79">Business Transformation</text><circle cx="276" cy="76.5" r="7" fill="var(--navy)"/>
    <rect x="152" y="90" width="142" height="13" rx="6.5" fill="#f4f5f8"/><text x="168" y="99">Design Authority</text><circle cx="288" cy="96.5" r="7" fill="var(--cyan)"/>
    <rect x="162" y="109" width="144" height="13" rx="6.5" fill="#f4f5f8"/><text x="179" y="118">Architecture &amp; Transition State</text><circle cx="300" cy="115.5" r="7" fill="var(--green)"/>
    <rect x="172" y="129" width="146" height="13" rx="6.5" fill="#f4f5f8"/><text x="188" y="138">Data Strategy &amp; Governance</text><circle cx="313" cy="135.5" r="7" fill="var(--slate)"/>
    <rect x="182" y="149" width="148" height="13" rx="6.5" fill="#f4f5f8"/><text x="200" y="158">Operational Stability &amp; Efficiencency</text><circle cx="324" cy="155.5" r="7" fill="var(--grey)"/>
    <rect x="192" y="169" width="150" height="13" rx="6.5" fill="#f4f5f8"/><text x="209" y="178">Operational Stability</text><circle cx="334" cy="175.5" r="7" fill="#707684"/>
  </g>
  <g>
    <polygon points="131,46 122,66 131,66" fill="#2f63dc"/><polygon points="131,46 140,66 131,66" fill="#1e44a8"/>
    <polygon points="122,68 113,88 131,88 131,68" fill="#1b2a5c"/><polygon points="140,68 149,88 131,88 131,68" fill="#243873"/>
    <polygon points="112,90 103,108 131,108 131,90" fill="#14c4ea"/><polygon points="150,90 159,108 131,108 131,90" fill="#10a9cc"/>
    <polygon points="102,110 93,128 131,128 131,110" fill="#1fbf7f"/><polygon points="160,110 169,128 131,128 131,110" fill="#18a36b"/>
    <polygon points="92,130 83,148 131,148 131,130" fill="#5b6a88"/><polygon points="170,130 179,148 131,148 131,130" fill="#4a5874"/>
    <polygon points="82,150 73,168 131,168 131,150" fill="#8896b3"/><polygon points="180,150 189,168 131,168 131,150" fill="#74829e"/>
    <polygon points="72,170 58,195 131,210 131,170" fill="#8e8f94"/><polygon points="190,170 204,195 131,210 131,170" fill="#6e7076"/>
  </g>
  <use href="#footer-brand" x="20" y="206" width="40" height="10"/>
  <text x="368" y="215" class="num">4</text>
  <use href="#corner" x="370" y="196" width="30" height="30"/>
</svg>
</section>

<!-- Table -->
<section class="slide r2 c2">
<svg viewBox="0 0 400 226">
  <text x="20" y="22" class="h" font-size="18">Cloud Assessments &amp; Advisory Services</text>
  <g font-family="Barlow Condensed,sans-serif" font-weight="600" font-size="7" fill="var(--blue)">
    <text x="23" y="43">Description</text><text x="203" y="43">Who</text><text x="242" y="43">01</text><text x="280" y="43">02</text><text x="317" y="43">03</text><text x="355" y="43">04</text>
  </g>
  <line x1="20" y1="46" x2="377" y2="46" stroke="var(--blue)" stroke-width=".6"/>
  <g fill="var(--band)">
    <rect x="20" y="51" width="357" height="8"/><rect x="20" y="86" width="357" height="8"/><rect x="20" y="116" width="357" height="8"/><rect x="20" y="146" width="357" height="8"/><rect x="20" y="175" width="357" height="8"/>
  </g>
  <g class="b" font-size="6">
    <text x="23" y="57">Project Startup (Internal)</text><text x="208" y="57" text-anchor="middle">Meiling</text>
    <text x="23" y="75">Operational Stability &amp; Efficiency (FlowMap / AMS/ Test)</text><text x="208" y="75" text-anchor="middle">Arjun</text>
    <text x="23" y="92">Threat Assessment &amp; Security</text><text x="208" y="92" text-anchor="middle">Tomas</text>
    <text x="23" y="107">Discovery / Process Mapping / Optimization</text><text x="208" y="107" text-anchor="middle">Priya</text>
    <text x="23" y="122">Data Strategy &amp; Governance</text><text x="208" y="122" text-anchor="middle">Ravi</text>
    <text x="23" y="137">Enterprise Architecture &amp; Transition State</text><text x="208" y="137" text-anchor="middle">Leo</text>
    <text x="23" y="152">Design Authority - KLV</text><text x="208" y="152" text-anchor="middle">Owen</text>
    <text x="23" y="167">Business Transformation - Finance</text><text x="208" y="167" text-anchor="middle">Owen</text>
    <text x="23" y="181">Business Transformation - Logistics</text><text x="208" y="181" text-anchor="middle">Leo, Kenji</text>
    <text x="23" y="196">ROI Realization / Board Level Advisory</text><text x="208" y="196" text-anchor="middle">Ana, Lim</text>
  </g>
  <line x1="20" y1="200" x2="377" y2="200" stroke="var(--blue)" stroke-width=".6"/>
  <use href="#footer-brand" x="20" y="206" width="40" height="10"/>
  <text x="368" y="215" class="num">5</text>
  <use href="#corner" x="370" y="196" width="30" height="30"/>
</svg>
</section>

<!-- Org chart -->
<section class="slide r2 c3">
<svg viewBox="0 0 400 226">
  <text x="20" y="22" class="h" font-size="18">Model for Each Country</text>
  <g stroke="var(--navy)" stroke-width=".8" fill="none">
    <path d="M199 70 V81 M73 91 V81 H325 V91 M199 81 V91"/>
  </g>
  <rect x="150" y="54" width="98" height="16" rx="8" fill="var(--blue)"/>
  <text x="199" y="64.5" text-anchor="middle" font-family="Barlow,sans-serif" font-weight="600" font-size="5" fill="#fff">Dana Reyes</text>
  <g font-family="Barlow,sans-serif" font-size="4.4" text-anchor="middle">
    <rect x="24" y="92" width="98" height="15" rx="7.5" fill="var(--navy)"/><text x="73" y="101" fill="#fff">Name Surname</text>
    <rect x="150" y="92" width="98" height="15" rx="7.5" fill="var(--cyan)"/><text x="199" y="101" fill="#fff">Name Surname</text>
    <rect x="277" y="92" width="98" height="15" rx="7.5" fill="var(--green)"/><text x="326" y="101" fill="#fff">Name Surname</text>
  </g>
  <g stroke-dasharray="1.5 1.5" stroke-width=".5" fill="none">
    <path d="M45 107 V180 M99 107 V180" stroke="#9aa6c4"/>
    <path d="M172 107 V180 M226 107 V180" stroke="#8fe0f2"/>
    <path d="M299 107 V180 M353 107 V180" stroke="#8fe3c1"/>
  </g>
  <g font-family="Barlow,sans-serif" font-size="4.4" text-anchor="middle" stroke-width=".7">
    <g stroke="#8f9bbd" fill="#fff">
      <rect x="24" y="118" width="43" height="16" rx="2"/><rect x="78" y="118" width="43" height="16" rx="2"/>
      <rect x="24" y="145" width="43" height="16" rx="2" fill="#b7c4e6"/><rect x="78" y="145" width="43" height="16" rx="2"/>
      <rect x="24" y="172" width="43" height="16" rx="2"/><rect x="78" y="172" width="43" height="16" rx="2" fill="#b7c4e6"/>
    </g>
    <g stroke="#6fd8ef" fill="#fff">
      <rect x="151" y="118" width="43" height="16" rx="2" fill="#b9eef9"/><rect x="205" y="118" width="43" height="16" rx="2"/>
      <rect x="151" y="145" width="43" height="16" rx="2"/><rect x="205" y="145" width="43" height="16" rx="2" fill="#b9eef9"/>
      <rect x="151" y="172" width="43" height="16" rx="2"/><rect x="205" y="172" width="43" height="16" rx="2"/>
    </g>
    <g stroke="#6fdcb0" fill="#fff">
      <rect x="278" y="118" width="43" height="16" rx="2"/><rect x="332" y="118" width="43" height="16" rx="2" fill="#bff0da"/>
      <rect x="278" y="145" width="43" height="16" rx="2"/><rect x="332" y="145" width="43" height="16" rx="2"/>
      <rect x="278" y="172" width="43" height="16" rx="2" fill="#bff0da"/><rect x="332" y="172" width="43" height="16" rx="2"/>
    </g>
    <g fill="#8a93a6">
      <text x="45.5" y="128">Name</text><text x="99.5" y="128">Name</text><text x="45.5" y="155">Name</text><text x="99.5" y="155">Name</text><text x="45.5" y="182">Name</text><text x="99.5" y="182">Name</text>
      <text x="172.5" y="128">Name</text><text x="226.5" y="128">Name</text><text x="172.5" y="155">Name</text><text x="226.5" y="155">Name</text><text x="172.5" y="182">Name</text><text x="226.5" y="182">Name</text>
      <text x="299.5" y="128">Name</text><text x="353.5" y="128">Name</text><text x="299.5" y="155">Name</text><text x="353.5" y="155">Name</text><text x="299.5" y="182">Name</text><text x="353.5" y="182">Name</text>
    </g>
  </g>
  <use href="#footer-brand" x="20" y="206" width="40" height="10"/>
  <text x="368" y="215" class="num">6</text>
  <use href="#corner" x="370" y="196" width="30" height="30"/>
</svg>
</section>

<!-- Demographics -->
<section class="slide r3 c1">
<svg viewBox="0 0 400 226">
  <rect width="400" height="226" fill="var(--panel)"/>
  <text x="20" y="22" class="h" font-size="18">Employee Demographics</text>
  <rect x="21" y="38" width="360" height="81" rx="2" fill="#fff"/>
  <text x="32" y="49" class="b" font-size="4.5" font-weight="600">Visits</text>
  <g class="b" font-size="4" fill="var(--mute)" text-anchor="end">
    <text x="44" y="61">5000</text><text x="44" y="69">4000</text><text x="44" y="77">3000</text><text x="44" y="84">2000</text><text x="44" y="92">1000</text><text x="44" y="100">0</text>
  </g>
  <g stroke-width="2.6">
    <path d="M57 99 V84 M74 99 V82 M91 99 V81 M109 99 V80 M126 99 V82 M144 99 V81 M161 99 V80 M178 99 V79 M195 99 V81 M212 99 V80 M230 99 V78 M247 99 V77" stroke="var(--navy)"/>
    <path d="M57 84 V78 M74 82 V75 M91 81 V73 M109 80 V72 M126 82 V71 M144 81 V72 M161 80 V70 M178 79 V70 M195 81 V70 M212 80 V69 M230 78 V62 M247 77 V61" stroke="var(--green)"/>
    <path d="M57 78 V76 M74 75 V74 M109 72 V70 M161 70 V68 M212 69 V68" stroke="var(--blue)"/>
  </g>
  <g class="b" font-size="4" fill="var(--mute)" text-anchor="middle">
    <text x="57" y="106">Jan</text><text x="74" y="106">Feb</text><text x="91" y="106">Mar</text><text x="109" y="106">Apr</text><text x="126" y="106">May</text><text x="144" y="106">Jun</text><text x="161" y="106">Jul</text><text x="178" y="106">Aug</text><text x="195" y="106">Sep</text><text x="212" y="106">Oct</text><text x="230" y="106">Nov</text><text x="247" y="106">Dec</text>
  </g>
  <line x1="265" y1="46" x2="265" y2="112" stroke="#e3e6ec" stroke-width=".5"/>
  <circle cx="307" cy="70" r="19" fill="none" stroke="#e7ebf2" stroke-width="3"/>
  <path d="M307 51 A19 19 0 0 1 324 78" fill="none" stroke="var(--navy)" stroke-width="3"/>
  <path d="M324 78 A19 19 0 0 1 300 88" fill="none" stroke="var(--cyan)" stroke-width="3"/>
  <path d="M300 88 A19 19 0 0 1 290 62" fill="none" stroke="var(--green)" stroke-width="3"/>
  <text x="307" y="71" text-anchor="middle" class="b" font-size="5" font-weight="600">55.000</text>
  <text x="307" y="77" text-anchor="middle" class="b" font-size="2.8" fill="var(--mute)">Audience</text>
  <g class="b" font-size="4" fill="var(--blue)">
    <text x="334" y="64">▪ Search Engines</text><text x="334" y="70">▪ Social Media</text><text x="334" y="76">▪ Direct</text><text x="334" y="82">▪ Other</text>
  </g>
  <g class="b" font-size="4">
    <line x1="275" y1="99" x2="275" y2="111" stroke="var(--navy)" stroke-width=".5"/><text x="278" y="104" font-weight="600">Text here</text><text x="278" y="110" fill="var(--mute)">09-23 03:53:25</text>
    <line x1="324" y1="99" x2="324" y2="111" stroke="var(--navy)" stroke-width=".5"/><text x="327" y="104" font-weight="600">Text here</text><text x="327" y="110" fill="var(--mute)">09-23 03:53:25</text>
  </g>
  <rect x="21" y="126" width="106" height="75" rx="2" fill="#7d87a0"/>
  <text x="74" y="147" text-anchor="middle" font-family="Barlow,sans-serif" font-weight="600" font-size="6" fill="#fff">Text More</text>
  <g font-family="Barlow,sans-serif" font-size="3.6" fill="#e6e9f0" text-anchor="middle">
    <text x="74" y="156">Short summary of the team profile,</text><text x="74" y="161">headcount and growth across regions,</text><text x="74" y="166">updated each quarter.</text>
  </g>
  <rect x="54" y="174" width="40" height="10" rx="5" fill="#fff"/>
  <text x="74" y="180.5" text-anchor="middle" font-family="Barlow,sans-serif" font-weight="600" font-size="3.8" fill="var(--navy)">Learn More</text>
  <g class="b">
    <rect x="133" y="126" width="121" height="34" rx="2" fill="#fff"/><text x="141" y="137" font-size="4.5" fill="var(--blue)" font-weight="600">Search</text><text x="141" y="147" font-size="8">2358946</text>
    <path d="M186 149 C195 143 200 142 204 146 C210 138 214 131 220 135 C228 140 236 135 246 136" fill="none" stroke="var(--blue)" stroke-width=".8"/>
    <rect x="260" y="126" width="121" height="34" rx="2" fill="#fff"/><text x="266" y="137" font-size="4.5" fill="var(--navy)" font-weight="600">Links</text><text x="266" y="147" font-size="8">2358946</text>
    <path d="M311 149 C318 141 322 140 326 146 C332 139 336 130 344 134 C352 140 360 135 370 137" fill="none" stroke="var(--navy)" stroke-width=".8"/>
    <rect x="133" y="166" width="121" height="35" rx="2" fill="#fff"/><text x="141" y="177" font-size="4.5" fill="var(--green)" font-weight="600">Social</text><text x="141" y="187" font-size="8">2358946</text>
    <path d="M186 189 C195 183 200 182 204 186 C210 178 214 171 220 175 C228 180 236 175 246 176" fill="none" stroke="var(--green)" stroke-width=".8"/>
    <rect x="260" y="166" width="121" height="35" rx="2" fill="#fff"/><text x="266" y="178" font-size="4.5" fill="var(--slate)" font-weight="600">Network Size</text><text x="266" y="188" font-size="8">2358946</text>
    <path d="M311 189 C318 181 322 180 326 186 C332 179 336 170 344 174 C352 180 360 175 370 177" fill="none" stroke="var(--slate)" stroke-width=".8"/>
  </g>
  <use href="#footer-brand" x="20" y="206" width="40" height="10"/>
  <text x="368" y="215" class="num">7</text>
  <use href="#corner" x="370" y="196" width="30" height="30"/>
</svg>
</section>

<!-- Timeline -->
<section class="slide r3 c2">
<svg viewBox="0 0 400 226">
  <text x="20" y="22" class="h" font-size="18">2026 High-level Timeline</text>
  <text x="29" y="46" class="b" font-size="4.2" fill="var(--mute)" letter-spacing="1.2">TASK</text>
  <g fill="#f1f3f6">
    <rect x="56" y="50" width="26" height="153"/><rect x="109" y="50" width="26" height="153"/><rect x="162" y="50" width="26" height="153"/><rect x="215" y="50" width="26" height="153"/><rect x="268" y="50" width="26" height="153"/><rect x="321" y="50" width="26" height="153"/>
  </g>
  <g fill="var(--blue)">
    <rect x="56" y="40" width="25.6" height="10" rx="1"/><rect x="82.7" y="40" width="25.6" height="10" rx="1"/><rect x="109.4" y="40" width="25.6" height="10" rx="1"/><rect x="136.1" y="40" width="25.6" height="10" rx="1"/><rect x="162.8" y="40" width="25.6" height="10" rx="1"/><rect x="189.5" y="40" width="25.6" height="10" rx="1"/><rect x="216.2" y="40" width="25.6" height="10" rx="1"/><rect x="242.9" y="40" width="25.6" height="10" rx="1"/><rect x="269.6" y="40" width="25.6" height="10" rx="1"/><rect x="296.3" y="40" width="25.6" height="10" rx="1"/><rect x="323" y="40" width="25.6" height="10" rx="1"/><rect x="349.7" y="40" width="25.6" height="10" rx="1"/>
  </g>
  <g font-family="Barlow,sans-serif" font-size="3.4" fill="#fff" text-anchor="middle">
    <text x="68.8" y="46.3">JAN</text><text x="95.5" y="46.3">FEB</text><text x="122.2" y="46.3">MAR</text><text x="148.9" y="46.3">APR</text><text x="175.6" y="46.3">MAY</text><text x="202.3" y="46.3">JUN</text><text x="229" y="46.3">JUL</text><text x="255.7" y="46.3">AUG</text><text x="282.4" y="46.3">SEP</text><text x="309.1" y="46.3">OCT</text><text x="335.8" y="46.3">NOV</text><text x="362.5" y="46.3">DEC</text>
  </g>
  <g class="b" font-size="4" fill="var(--mute)">
    <text x="26" y="72">Description</text><text x="26" y="98">Description</text><text x="26" y="124">Description</text><text x="26" y="150">Description</text><text x="26" y="176">Description</text>
  </g>
  <g stroke="var(--red)" stroke-width=".6">
    <line x1="135" y1="50" x2="135" y2="200"/><line x1="215" y1="50" x2="215" y2="200"/><line x1="294" y1="50" x2="294" y2="200"/><line x1="373" y1="50" x2="373" y2="200"/>
  </g>
  <g fill="var(--red)">
    <rect x="128" y="196" width="14" height="9" rx="4.5"/><rect x="208" y="196" width="14" height="9" rx="4.5"/><rect x="287" y="196" width="14" height="9" rx="4.5"/><rect x="366" y="196" width="14" height="9" rx="4.5"/>
  </g>
  <g font-family="Barlow,sans-serif" font-size="3.2" fill="#fff" text-anchor="middle">
    <text x="135" y="201.8">01</text><text x="215" y="201.8">02</text><text x="294" y="201.8">03</text><text x="373" y="201.8">04</text>
  </g>
  <g fill="#fff" stroke="#e6e9ef" stroke-width=".4">
    <rect x="63" y="63" width="63" height="80" rx="2"/><rect x="142" y="63" width="64" height="115" rx="2"/><rect x="222" y="63" width="64" height="63" rx="2"/><rect x="302" y="63" width="64" height="55" rx="2"/>
  </g>
  <g font-family="Barlow Condensed,sans-serif" font-weight="600" font-size="8" fill="var(--blue)">
    <text x="113" y="72">01</text><text x="193" y="72">02</text><text x="273" y="72">03</text><text x="353" y="72">04</text>
  </g>
  <g class="b" font-size="3.9">
    <text x="69" y="74">• Vela Toolkit</text><text x="69" y="80.5">• Assessments Ready</text><text x="69" y="87">• Onboard Australia</text><text x="71" y="93">MD</text><text x="69" y="99.5">• Translate to</text><text x="71" y="105.5">Japanese</text><text x="69" y="112">• Deliver 1 Assessment</text><text x="71" y="118">/ Mth by Australia</text><text x="69" y="124.5">• Establish Career</text><text x="71" y="130.5">Path &amp; Skills Matrix</text>
    <text x="148" y="74">• New Japan MD hired</text><text x="148" y="80.5">• Target Japanese</text><text x="150" y="86.5">companies for</text><text x="150" y="92.5">assessment to</text><text x="150" y="98.5">prepare for</text><text x="150" y="104.5">2027budget cycle</text><text x="148" y="111">• Deliver 1</text><text x="150" y="117">Assessment/ Mth by</text><text x="150" y="123">Japan</text><text x="148" y="129.5">• Build Methods and</text><text x="150" y="135.5">Standardize Delivery</text><text x="150" y="141.5">Model</text><text x="148" y="148">• Sell 1 Advisory</text><text x="150" y="154">Services in Australia</text>
    <text x="228" y="74">• First Public Cloud</text><text x="230" y="80">mid-market in</text><text x="230" y="86">Australia</text><text x="228" y="92.5">• Sell 1 Advisory</text><text x="230" y="98.5">Services in Japan</text><text x="228" y="105">• Sell 1 Advisory</text><text x="230" y="111">Service in Australia</text>
    <text x="308" y="74">• Second Public Cloud</text><text x="310" y="80">in Australia</text><text x="308" y="86.5">• Sell 2 Advisory</text><text x="310" y="92.5">Services in Japan</text><text x="308" y="99">• Sell 1 Advisory</text><text x="310" y="105">Services in Australia</text>
  </g>
  <use href="#footer-brand" x="20" y="206" width="40" height="10"/>
  <text x="368" y="215" class="num">8</text>
  <use href="#corner" x="370" y="196" width="30" height="30"/>
</svg>
</section>

<!-- Quote -->
<section class="slide r3 c3">
<svg viewBox="0 0 400 226">
  <rect x="166" y="23" width="234" height="178" fill="url(#photoTone)" role="img" aria-label="Photo of a cheerful, diverse business team working together at a laptop"/>
  <path d="M0 23 H200 L222 113 L180 201 H0 Z" fill="url(#blueFade)"/>
  <polygon points="168,23 205,23 238,113 213,113" fill="#7fa3ee" opacity=".7"/>
  <polygon points="213,113 238,113 202,201 178,201" fill="var(--blue)" opacity=".8"/>
  <polygon points="162,0 176,0 200,23 186,23" fill="#c7d5f5"/>
  <polygon points="0,23 90,23 20,201 0,201" fill="#4d7be6" opacity=".35"/>
  <g font-family="Barlow,sans-serif" font-style="italic" font-weight="700" font-size="8" fill="#fff" text-anchor="middle">
    <text x="100" y="66">The Stars Will Never Align, And The Traffic</text>
    <text x="100" y="81">Lights Of Life Will Never All Be Green At</text>
    <text x="100" y="96">The Same Time. The Universe Doesn’t</text>
    <text x="100" y="111">Conspire Against You, But It Doesn’t Go</text>
    <text x="100" y="126">Out Of Its Way To Line Up The Pins Either.</text>
    <text x="100" y="141">Conditions Are Never Perfect</text>
  </g>
  <rect x="74" y="162" width="52" height="10" rx="5" fill="var(--green)"/>
  <text x="100" y="168.6" text-anchor="middle" font-family="Barlow,sans-serif" font-size="3.8" fill="#7be0b2">Let's Talk</text>
  <use href="#footer-brand" x="20" y="206" width="40" height="10"/>
  <text x="368" y="215" class="num">9</text>
  <use href="#corner" x="370" y="196" width="30" height="30"/>
</svg>
</section>

<!-- Three pillars -->
<section class="slide r4 c1">
<svg viewBox="0 0 400 226">
  <polygon points="0,3 98,3 88,17 0,17" fill="url(#blueFade)"/>
  <rect x="0" y="30" width="400" height="92" fill="url(#officeTone)" role="img" aria-label="Photo of colleagues smiling at a computer monitor in an office"/>
  <rect x="8" y="120" width="381" height="52" fill="var(--blue)"/>
  <rect x="135" y="120" width="127" height="52" fill="var(--blue-dark)"/>
  <rect x="262" y="120" width="127" height="52" fill="#203f99"/>
  <g font-family="Barlow,sans-serif" font-weight="600" font-size="13" fill="#fff">
    <text x="14" y="144">01</text><text x="140" y="144">02</text><text x="267" y="144">03</text>
  </g>
  <g font-family="Barlow,sans-serif" font-size="3.8" fill="var(--cyan)">
    <text x="41" y="139">Target Audience</text><text x="168" y="139">Product &amp; Service</text><text x="296" y="139">Unique Product &amp; Service</text>
  </g>
  <g font-family="Barlow,sans-serif" font-size="3.9" fill="#fff">
    <text x="17" y="154">Economics, A Market Is A Composition Of Systems,</text><text x="17" y="160">Institutions, Procedures, Social Relations</text>
    <text x="143" y="154">Economics, A Market Is A Composition Of Systems,</text><text x="143" y="160">Institutions, Procedures, Social Relations</text>
    <text x="270" y="154">Economics, A Market Is A Composition Of Systems,</text><text x="270" y="160">Institutions, Procedures, Social Relations</text>
  </g>
  <use href="#footer-brand" x="20" y="206" width="40" height="10"/>
  <text x="368" y="215" class="num">10</text>
  <use href="#corner" x="370" y="196" width="30" height="30"/>
</svg>
</section>

<!-- Closing -->
<section class="slide r4 c2">
<svg viewBox="0 0 400 226">
  <polygon points="197,0 400,0 400,226 365,226" fill="#c7d5f5"/>
  <polygon points="235,0 290,0 400,120 400,200" fill="var(--blue)"/>
  <polygon points="330,0 400,0 400,60" fill="#7a8fbd"/>
  <polygon points="300,226 400,120 400,226" fill="#8ea6de"/>
  <polygon points="284,13 354,83 284,153 214,83" fill="#fff"/>
  <polygon points="284,20 347,83 284,146 221,83" fill="url(#officeTone)" role="img" aria-label="Photo of two colleagues collaborating at a desk in a warmly lit office"/>
  <circle cx="30" cy="87" r="8" fill="var(--blue)"/>
  <text x="44" y="95" class="brand" font-size="22">VELA</text>
  <text x="22" y="149" font-family="Barlow,sans-serif" font-weight="600" font-size="32" fill="var(--blue)">Thank you!</text>
</svg>
</section>

</main>
</body>
</html>
```